Qarnetix EIRL Business Card Design Project

We need a business card design for a New Business Intelligence Consultant. We bring a complete service to the client from first consulting meeting to help desk and system improvement.

I will upload the company logo and I like to use the logo colors on the card. Feel free to use all logo components on the design, for example one side with the black logo using complete card and the other side only the red shape (is an example, feel absolutely free :)).

The principal idea is to sell a professional service and a modern company.

Target Market(s)

IT Business Intelligence Clients

Industry/Entity Type

Professional Service

Requirements
Nice to have
• - Use the logo colors and minimize white sections.
- Rounded borders
Should not have
• I don't want to see any references to people working on a meeting or office photos or any computers related logos.

```html
<!DOCTYPE html>
<html lang="en">
<head>
<meta charset="utf-8">
<title>Qarnetix EIRL – Business Card</title>
<link rel="stylesheet" href="https://fonts.googleapis.com/css2?family=Open+Sans:ital,wght@0,400;0,600;0,700;1,400&display=swap">
<style>
  :root {
    --bg-light: #f4f4f4;
    --bg-dark: #b9b9b9;
    --card-black: #1d1d1d;
    --card-black-soft: #262626;
    --brand-red: #e31e26;
    --brand-red-soft: #ea2a30;
    --brand-grey: #9a9a9a;
    --ink-dark: #111111;
    --ink-light: #f2f2f2;
    --label-ink: #1a1a1a;
  }
  * { box-sizing: border-box; margin: 0; padding: 0; }
  html, body { width: 1200px; height: 900px; overflow: hidden; }
  body {
    position: relative;
    background: radial-gradient(ellipse at 50% 40%, var(--bg-light) 0%, #dcdcdc 55%, var(--bg-dark) 100%);
    font-family: "Open Sans", Arial, sans-serif;
  }
  .card {
    position: absolute;
    border-radius: 30px;
    overflow: hidden;
    box-shadow: 0 6px 14px rgba(0,0,0,0.35);
  }
  /* Side 1 – front */
  .card-front {
    left: 28px; top: 48px; width: 716px; height: 396px;
    background: var(--card-black);
    display: flex; align-items: center; justify-content: center;
  }
  .card-front .texture {
    position: absolute; inset: 0;
    background: radial-gradient(ellipse at 50% 50%, var(--card-black-soft), var(--card-black));
  }
  .front-brand {
    position: relative;
    display: flex; align-items: center; gap: 22px;
  }
  .brand-square {
    display: block; background: var(--brand-red);
  }
  .front-brand .brand-square { width: 54px; height: 54px; }
  .front-brand .brand-name {
    font-size: 78px; font-weight: 600; color: var(--brand-grey);
    letter-spacing: -1px; line-height: 1;
  }
  /* Side 2 – back */
  .card-back {
    left: 484px; top: 460px; width: 692px; height: 400px;
    background: var(--card-black);
  }
  .contact-panel {
    position: absolute; left: 0; top: 0; width: 100%; height: 244px;
    background: var(--brand-red);
  }
  .contact-panel .texture {
    position: absolute; inset: 0;
    background: radial-gradient(ellipse at 50% 40%, var(--brand-red-soft), var(--brand-red));
  }
  .person {
    position: absolute; left: 32px; top: 22px; color: var(--ink-dark);
  }
  .person-name { font-size: 29px; font-weight: 700; line-height: 1.2; }
  .person-role, .person-email {
    font-size: 16px; font-style: italic; line-height: 1.55;
  }
  .person-role { margin-top: 6px; }
  .details {
    position: absolute; right: 32px; top: 64px;
    text-align: right; font-size: 22px; line-height: 33px; color: var(--ink-dark);
    list-style: none;
  }
  .details strong { font-weight: 700; }
  .brand-band {
    position: absolute; left: 0; top: 244px; width: 100%; height: 156px;
    display: flex; align-items: center; padding-left: 30px; gap: 26px;
  }
  .brand-band .brand-square { width: 84px; height: 84px; }
  .brand-band .brand-name {
    font-size: 76px; font-weight: 400; color: var(--brand-grey);
    letter-spacing: -1px; line-height: 1;
  }
  .side-label {
    position: absolute; font-family: "Open Sans", Arial, sans-serif;
    font-style: italic; font-size: 34px; color: var(--label-ink);
  }
  .label-front { left: 740px; top: 58px; }
  .label-back { left: 362px; top: 796px; }
</style>
</head>
<body>
  <section class="card card-front" aria-label="Card side 1">
    <div class="texture" role="img" aria-label="Dark hexagon texture pattern"></div>
    <div class="front-brand">
      <span class="brand-square"></span>
      <span class="brand-name">qarnetix</span>
    </div>
  </section>
  <span class="side-label label-front">Side 1</span>

  <section class="card card-back" aria-label="Card side 2">
    <div class="contact-panel">
      <div class="texture" role="img" aria-label="Red hexagon texture pattern"></div>
      <div class="person">
        <h1 class="person-name">Daniel Moreau</h1>
        <p class="person-role">Job Title</p>
        <p class="person-email">Email: daniel.moreau@qarnetix.com</p>
      </div>
      <ul class="details">
        <li>Ph: <strong>555-555-5555</strong></li>
        <li>Fax: <strong>555-555-5556</strong></li>
        <li>Address Line 1</li>
        <li>Address Line 2</li>
        <li>City, State&nbsp; 00001</li>
      </ul>
    </div>
    <div class="brand-band">
      <span class="brand-square"></span>
      <span class="brand-name">qarnetix</span>
    </div>
  </section>
  <span class="side-label label-back">Side 2</span>
</body>
</html>
```